Business card for job seeker professional

Hi. I'm a sale and marketing professional who's just moved to Australia and looking for a job. I would like to have a business card designed for me, which I can use for job interviews/networking. Given Pravolink increasing importance in the job market, I would like my public profile link (http://au.pravolink-net.com/in/tomasveridun/) to be incorporated into my details.

```html
<!DOCTYPE html>
<html lang="en">
<head>
<meta charset="utf-8">
<title>Tomas Veridun – Business Card</title>
<link rel="stylesheet" href="https://fonts.googleapis.com/css2?family=Cantarell:wght@400;700&display=swap">
<style>
  :root {
    --brand-green: #1d6b37;
    --text-green: #1f6a36;
    --ink: #111111;
    --link-blue: #1f5f9c;
    --paper: #ffffff;
    --arrow-green: #2a8a31;
    --arrow-shade: #e4e4e4;
  }
  * { margin: 0; padding: 0; box-sizing: border-box; }
  html, body { width: 1200px; height: 693px; overflow: hidden; background: var(--paper); }
  .card {
    position: relative;
    width: 1200px;
    height: 693px;
    background: var(--paper);
    font-family: "Cantarell", "Trebuchet MS", sans-serif;
    font-variant-numeric: lining-nums;
    overflow: hidden;
  }
  .name-band {
    position: absolute;
    left: 0; top: 0;
    width: 1200px; height: 266px;
    background: var(--brand-green);
    display: flex;
    align-items: center;
    justify-content: center;
  }
  .name-band__name {
    color: var(--paper);
    font-weight: 400;
    font-size: 76px;
    line-height: 1;
    margin-top: -26px;
  }
  .expertise {
    position: absolute;
    top: 280px; left: 0;
    width: 1200px;
    text-align: center;
    color: var(--ink);
    font-size: 22px;
    line-height: 32px;
    font-weight: 400;
    white-space: nowrap;
  }
  .contact {
    position: absolute;
    left: 30px; top: 402px;
    list-style: none;
    color: var(--text-green);
    font-weight: 400;
  }
  .contact__item { font-size: 34px; line-height: 50px; }
  .contact__item--email { font-size: 31px; line-height: 56px; }
  .profile-link {
    position: absolute;
    left: 30px; top: 618px;
    display: flex;
    align-items: center;
    gap: 12px;
    color: var(--link-blue);
    font-size: 28px;
    line-height: 56px;
    font-weight: 400;
    white-space: nowrap;
  }
  .profile-link__mark {
    width: 44px; height: 44px;
    background: var(--link-blue);
    border-radius: 5px;
    flex: none;
  }
  .growth-visual {
    position: absolute;
    left: 752px; top: 384px;
    width: 400px; height: 309px;
    background: linear-gradient(30deg, var(--arrow-green) 0%, #7fbf83 45%, var(--arrow-shade) 75%, var(--paper) 100%);
    opacity: 0.85;
  }
</style>
</head>
<body>
  <main class="card">
    <header class="name-band">
      <h1 class="name-band__name">Tomas Veridun</h1>
    </header>

    <p class="expertise">Business Strategy | International Business Development | Marketing and Communication</p>

    <ul class="contact">
      <li class="contact__item">Melbourne, Australia</li>
      <li class="contact__item">0491 570 156</li>
      <li class="contact__item contact__item--email">tomas@veridun.au</li>
    </ul>

    <p class="profile-link">
      <span class="profile-link__mark" aria-hidden="true"></span>
      <span class="profile-link__network">Pravolink</span>
      <span class="profile-link__url">au.pravolink-net.com/in/tomasveridun</span>
    </p>

    <div class="growth-visual" role="img" aria-label="3D green zigzag arrow rising to the upper right with a soft shadow, symbolising growth"></div>
  </main>
</body>
</html>
```